We need a design for our security installation based business. Our name is K M Security Systems

We need a business card for a security installation based company. We want to look modern and professional. We would like our company logo used and the three main colours to be white, black and orange. We install intruder alarms, cctv and access control. Our preference would be to use the black/orange design on the front and orange/black on the back. Feel free to post variations.

Target Market(s)

Business owners, commercial property and large residential properties

Industry/Entity Type

Business

Contact Information for Business Card

Owen Pelham 07813 592 640

Liam Fenwick 07751 286 419

operations@kmsecuritysystems.co.uk

Intruder Alarms
CCTV
Access Control

Colors
f78f20
000000
ffffff

Requirements
Must have
• Must have the logo on the business card somewhere

```html
<!DOCTYPE html>
<html lang="en">
<head>
<meta charset="utf-8">
<title>K M Security Systems – Business Card</title>
<link rel="stylesheet" href="https://fonts.googleapis.com/css2?family=Lato:wght@400;700&display=swap">
<style>
  :root {
    --backdrop: #1c1c1c;
    --orange: #ef4f26;
    --black: #000000;
    --white: #ffffff;
    --rule: #8a8a8a;
  }
  * { box-sizing: border-box; margin: 0; padding: 0; }
  html, body {
    width: 1200px; height: 1200px; overflow: hidden;
    background: var(--backdrop);
    font-family: "Lato", sans-serif;
  }
  .sheet {
    width: 1200px; height: 1200px;
    display: flex; flex-direction: column;
    align-items: center; justify-content: center; gap: 48px;
  }
  .card {
    width: 900px; height: 514px;
    position: relative;
    box-shadow: 0 18px 40px rgba(0,0,0,.55);
  }
  /* Front */
  .card--front {
    background: var(--orange);
    display: flex; flex-direction: column; align-items: center; justify-content: center;
  }
  .brand-mark {
    width: 96px; height: 96px; background: var(--black); margin-bottom: 26px;
  }
  .brand-name {
    color: var(--black); font-weight: 700; text-transform: uppercase;
    text-align: center; line-height: 1.1;
  }
  .brand-name__main { display: block; font-size: 64px; letter-spacing: 1px; }
  .brand-name__sub { display: block; font-size: 34px; letter-spacing: 12px; margin-top: 6px; }

  /* Back */
  .card--back {
    background: var(--black); color: var(--white);
    display: flex; flex-direction: column; align-items: center;
    padding-top: 62px;
  }
  .card--back .brand-name { color: var(--orange); }
  .card--back .brand-name__main { font-size: 52px; }
  .card--back .brand-name__sub { font-size: 28px; letter-spacing: 10px; }

  .contacts {
    display: flex; align-items: center; gap: 44px; margin-top: 36px;
  }
  .contact { display: flex; flex-direction: column; gap: 8px; }
  .contact--left { align-items: flex-end; }
  .contact--right { align-items: flex-start; }
  .contact__name {
    color: var(--orange); font-weight: 700; font-size: 30px; text-transform: uppercase;
  }
  .contact__phone {
    display: flex; align-items: center; gap: 12px; font-size: 24px; letter-spacing: 1px;
  }
  .contacts__divider { width: 1px; height: 80px; background: var(--rule); }
  .icon { width: 26px; height: 26px; flex: none; }

  .email {
    display: flex; align-items: center; gap: 14px;
    margin-top: 28px; font-size: 24px;
  }
  .services {
    margin-top: 34px; font-size: 26px; letter-spacing: 3px;
  }
  .services__sep { color: var(--orange); margin: 0 12px; }
</style>
</head>
<body>
<main class="sheet">

  <section class="card card--front" aria-label="Card front">
    <div class="brand-mark" aria-hidden="true"></div>
    <h1 class="brand-name">
      <span class="brand-name__main">K M Security</span>
      <span class="brand-name__sub">Systems</span>
    </h1>
  </section>

  <section class="card card--back" aria-label="Card back">
    <h2 class="brand-name">
      <span class="brand-name__main">K M Security</span>
      <span class="brand-name__sub">Systems</span>
    </h2>

    <div class="contacts">
      <div class="contact contact--left">
        <span class="contact__name">Owen Pelham</span>
        <span class="contact__phone">07813 592 640
          <svg class="icon" viewBox="0 0 24 24" aria-hidden="true"><path d="M6.6 10.8a15 15 0 0 0 6.6 6.6l2.2-2.2a1 1 0 0 1 1-.25 11.4 11.4 0 0 0 3.6.57 1 1 0 0 1 1 1V20a1 1 0 0 1-1 1A17 17 0 0 1 3 4a1 1 0 0 1 1-1h3.5a1 1 0 0 1 1 1c0 1.25.2 2.45.57 3.57a1 1 0 0 1-.25 1z" fill="#ef4f26"/></svg>
        </span>
      </div>
      <div class="contacts__divider" aria-hidden="true"></div>
      <div class="contact contact--right">
        <span class="contact__name">Liam Fenwick</span>
        <span class="contact__phone">
          <svg class="icon" viewBox="0 0 24 24" aria-hidden="true"><path d="M6.6 10.8a15 15 0 0 0 6.6 6.6l2.2-2.2a1 1 0 0 1 1-.25 11.4 11.4 0 0 0 3.6.57 1 1 0 0 1 1 1V20a1 1 0 0 1-1 1A17 17 0 0 1 3 4a1 1 0 0 1 1-1h3.5a1 1 0 0 1 1 1c0 1.25.2 2.45.57 3.57a1 1 0 0 1-.25 1z" fill="#ef4f26"/></svg>
          07751 286 419</span>
      </div>
    </div>

    <p class="email">
      <svg class="icon" viewBox="0 0 24 24" aria-hidden="true"><rect x="2" y="5" width="20" height="14" rx="1.5" fill="#ef4f26"/><path d="M3 6.5l9 6.5 9-6.5" fill="none" stroke="#000" stroke-width="1.6"/></svg>
      operations@kmsecuritysystems.co.uk
    </p>

    <p class="services">Intruder Alarms<span class="services__sep">|</span>CCTV<span class="services__sep">|</span>Access Control</p>
  </section>

</main>
</body>
</html>
```